Kestrel Photography Business Card

I need a business card designed for a photography business based in Perth, Western Australia called Kestrel Photography.

We specialise in wedding, event photography and portrait photography.

The business card must borrow the style of the attached logo.

The hex codes for the colours in the logo are:
#ED1D85 - Pink
#89C23E - Green
#37282F - Black

The name on the card will be:
Name: Toviran
Phone: 0417395268
Website: www.kestrelphotography.com.au
Facebook: kestrelphotography

I am open and happy to accept creative concepts.

I’d like some space at the back for writing notes and appointment details.

```html
<!DOCTYPE html>
<html lang="en">
<head>
<meta charset="utf-8">
<title>Kestrel Photography Business Card</title>
<link rel="stylesheet" href="https://fonts.googleapis.com/css2?family=Raleway:wght@300;400;500&display=swap">
<style>
  :root {
    --canvas-bg: #e9e5e7;
    --card-dark: #2f232a;
    --card-glow: #4d3d47;
    --ink-light: #f3eef1;
    --notes-panel: #a39aa0;
    --notes-edge: #b1a9ae;
    --icon-fill: #d8d2d6;
  }
  * { box-sizing: border-box; margin: 0; padding: 0; }
  html, body {
    width: 1200px; height: 1000px; overflow: hidden;
    background: var(--canvas-bg);
    font-family: "Raleway", sans-serif;
  }
  .stage {
    width: 1200px; height: 1000px;
    display: flex; align-items: center; justify-content: center; gap: 44px;
  }
  .card {
    position: relative;
    width: 530px; height: 320px;
    border-radius: 7px;
    background: radial-gradient(ellipse 70% 75% at 50% 42%, var(--card-glow), var(--card-dark));
    box-shadow: 0 6px 18px rgba(0,0,0,0.25);
    color: var(--ink-light);
    overflow: hidden;
  }
  /* Front */
  .card-front { text-align: center; }
  .brand-mark {
    position: absolute; left: 50%; top: 44px; transform: translateX(-50%);
    width: 84px; height: 84px;
  }
  .brand-wordmark {
    position: absolute; left: 0; right: 0; top: 152px;
    font-size: 15px; font-weight: 400; letter-spacing: 0.42em;
    text-transform: uppercase; padding-left: 0.42em;
  }
  .contact-name {
    position: absolute; left: 0; right: 0; top: 220px;
    font-size: 21px; font-weight: 500; letter-spacing: 0.06em;
    text-transform: uppercase;
  }
  .contact-phone {
    position: absolute; left: 0; right: 0; top: 252px;
    font-size: 14px; font-weight: 400; letter-spacing: 0.05em;
    display: flex; align-items: center; justify-content: center; gap: 4px;
  }
  .contact-phone svg { width: 15px; height: 15px; }
  /* Back */
  .card-back { background: var(--card-dark); }
  .notes-area {
    position: absolute; left: 11px; right: 11px; top: 11px; height: 258px;
    border-radius: 7px;
    background: radial-gradient(ellipse at 50% 45%, var(--notes-edge), var(--notes-panel));
  }
  .back-footer {
    position: absolute; left: 16px; right: 16px; bottom: 14px;
    display: flex; justify-content: space-between; align-items: center;
    font-size: 11px; letter-spacing: 0.08em; text-transform: uppercase;
  }
  .footer-item { display: flex; align-items: center; gap: 7px; }
  .footer-item svg { width: 13px; height: 13px; }
</style>
</head>
<body>
<main class="stage">
  <section class="card card-front" aria-label="Business card front">
    <svg class="brand-mark" viewBox="0 0 84 84" aria-hidden="true">
      <circle cx="42" cy="42" r="40" fill="none" stroke="var(--ink-light)" stroke-width="2"/>
    </svg>
    <h1 class="brand-wordmark">Kestrel Photography</h1>
    <p class="contact-name">Toviran</p>
    <p class="contact-phone">
      <svg viewBox="0 0 16 16" aria-hidden="true">
        <circle cx="8" cy="8" r="7" fill="none" stroke="var(--ink-light)" stroke-width="1.2"/>
        <path d="M5.2 4.3l1.3-.4.9 2-.9.7c.4.9 1.1 1.6 2 2l.7-.9 2 .9-.4 1.3c-3 .2-5.8-2.6-5.6-5.6z" fill="var(--ink-light)"/>
      </svg>
      0417395268
    </p>
  </section>

  <section class="card card-back" aria-label="Business card back">
    <div class="notes-area" role="img" aria-label="Blank panel for writing notes and appointment details"></div>
    <div class="back-footer">
      <span class="footer-item">
        <svg viewBox="0 0 14 14" aria-hidden="true">
          <circle cx="7" cy="7" r="6" fill="none" stroke="var(--icon-fill)" stroke-width="1.1"/>
          <ellipse cx="7" cy="7" rx="2.6" ry="6" fill="none" stroke="var(--icon-fill)" stroke-width="0.9"/>
          <line x1="1" y1="7" x2="13" y2="7" stroke="var(--icon-fill)" stroke-width="0.9"/>
        </svg>
        www.kestrelphotography.com.au
      </span>
      <span class="footer-item">
        <svg viewBox="0 0 14 14" aria-hidden="true">
          <circle cx="7" cy="7" r="6" fill="var(--icon-fill)"/>
        </svg>
        kestrelphotography
      </span>
    </div>
  </section>
</main>
</body>
</html>
```